We need a business card design for a Dubai based company .

We need a business card for a Dubai based company called "Zernova Smoking Requisites Trading LLC". We mainly import Flavoured Tobacco products and Charcoal which is used for smoking in a Hookah/Shisha and distribute to the wholesalers and retailers. Logo file is attached herewith.

```html
<!DOCTYPE html>
<html lang="en">
<head>
<meta charset="utf-8">
<title>Zernova Smoking Requisites Trading LLC — Business Card</title>
<link rel="stylesheet" href="https://fonts.googleapis.com/css2?family=Open+Sans:wght@400;700&display=swap">
<style>
  :root {
    --canvas: #e9e6e2;
    --card-white: #ffffff;
    --ink: #2b2b2b;
    --ink-soft: #3a3a3a;
    --accent-red: #b3191e;
    --band-black: #0d0d0d;
    --back-black: #0a0a0a;
    --back-edge: #1c1c1c;
    --on-dark: #ffffff;
  }
  * { box-sizing: border-box; margin: 0; padding: 0; }
  html, body {
    width: 1200px; height: 1017px; overflow: hidden;
    background: var(--canvas);
    font-family: "Open Sans", Arial, sans-serif;
  }
  .sheet {
    width: 1200px; height: 1017px;
    display: flex; flex-direction: column; align-items: center; justify-content: center;
    gap: 44px;
  }
  .card {
    position: relative;
    width: 760px; height: 434px;
    overflow: hidden;
    box-shadow: 0 6px 18px rgba(0,0,0,0.18);
  }

  /* Front */
  .card--front { background: var(--card-white); }
  .brand-name {
    position: absolute; left: 44px; top: 120px;
    width: 270px;
    color: var(--ink);
    font-size: 24px; font-weight: 700; line-height: 1.25;
  }
  .divider {
    position: absolute; left: 340px; top: 80px;
    width: 2px; height: 210px; background: var(--accent-red);
  }
  .contact { position: absolute; left: 372px; top: 70px; color: var(--ink-soft); }
  .contact__name { font-size: 27px; font-weight: 700; color: var(--ink); line-height: 1.15; }
  .contact__title { font-size: 18px; color: var(--accent-red); line-height: 1.35; margin-bottom: 16px; }
  .contact__address { font-size: 18px; line-height: 1.28; margin-bottom: 12px; }
  .contact__list { list-style: none; font-size: 18px; line-height: 1.25; }
  .contact__list li { display: flex; align-items: center; gap: 10px; }
  .contact__list svg { width: 14px; height: 14px; fill: var(--accent-red); flex: 0 0 14px; }
  .wave { position: absolute; left: 0; bottom: 0; width: 760px; height: 120px; }

  /* Back */
  .card--back {
    background: radial-gradient(ellipse at 45% 40%, var(--back-edge) 0%, var(--back-black) 75%);
    display: flex; align-items: center; justify-content: center;
  }
  .back-name {
    width: 420px; text-align: center;
    color: var(--on-dark);
    font-size: 32px; font-weight: 700; line-height: 1.25;
  }
</style>
</head>
<body>
<main class="sheet">

  <section class="card card--front" aria-label="Business card front">
    <p class="brand-name">Zernova Smoking Requisites Trading LLC</p>

    <div class="divider"></div>

    <div class="contact">
      <p class="contact__name">Your Name Here</p>
      <p class="contact__title">Managing Director</p>
      <p class="contact__address">418 Palm Crest Avenue,<br>Suite 210 Deira, Dubai</p>
      <ul class="contact__list">
        <li><svg viewBox="0 0 24 24"><path d="M6.6 10.8a15.1 15.1 0 0 0 6.6 6.6l2.2-2.2a1 1 0 0 1 1-.25 11.4 11.4 0 0 0 3.6.57 1 1 0 0 1 1 1V20a1 1 0 0 1-1 1A17 17 0 0 1 3 4a1 1 0 0 1 1-1h3.5a1 1 0 0 1 1 1c0 1.250.2 2.45.57 3.57a1 1 0 0 1-.25 1z"/></svg>(704) 555-0182</li>
        <li><svg viewBox="0 0 24 24"><path d="M7 1h10a2 2 0 0 1 2 2v18a2 2 0 0 1-2 2H7a2 2 0 0 1-2-2V3a2 2 0 0 1 2-2zm0 3v14h10V4zm5 15.5a1.2 1.2 0 1 0 0 2.4 1.2 1.2 0 0 0 0-2.4z"/></svg>(704) 555-0182</li>
        <li><svg viewBox="0 0 24 24"><path d="M2 5h20v14H2zm2 2v.5l8 5 8-5V7l-8 5z"/></svg>youremail@youremail.com</li>
        <li><svg viewBox="0 0 24 24"><path d="M12 2a10 10 0 1 0 0 20 10 10 0 0 0 0-20zm6.9 9h-3a15 15 0 0 0-1.3-5.6A8 8 0 0 1 18.9 11zM12 4c.9 1.2 1.8 3.6 1.9 7h-3.8C10.2 7.6 11.1 5.2 12 4zM9.4 5.4A15 15 0 0 0 8.1 11h-3a8 8 0 0 1 4.3-5.6zM5.1 13h3a15 15 0 0 0 1.3 5.6A8 8 0 0 1 5.1 13zM12 20c-.9-1.2-1.8-3.6-1.9-7h3.8c-.1 3.4-1 5.8-1.9 7zm2.6-1.4a15 15 0 0 0 1.3-5.6h3a8 8 0 0 1-4.3 5.6z"/></svg>www.yourwebsite.com</li>
      </ul>
    </div>

    <svg class="wave" viewBox="0 0 760 120" preserveAspectRatio="none" aria-hidden="true">
      <path d="M0,14 C180,2 420,22 760,86 L760,120 L0,120 Z" fill="var(--band-black)"/>
      <path d="M60,26 C300,16 540,44 760,68 L760,92 C560,56 330,30 60,26 Z" fill="var(--accent-red)"/>
    </svg>
  </section>

  <section class="card card--back" aria-label="Business card back">
    <p class="back-name">Zernova Smoking Requisites Trading LLC</p>
  </section>

</main>
</body>
</html>
```